Alapca breeding needs a website

Presentation of the farm, animals (stallions, mares, information about the animals, for sale) and possible later expansion with a webshop (alpaca wool products). We want to present our farm and the animals on the farm on this page. A mission why we are doing this. Furthermore, each animal should be shown with a picture and described. Later we want to sell our own products made from alpaca wool via a webshop. But we still need to grow a bit to do that.

Target Market(s)

Information about my alpaca breeding and the alpaca farm

Industry/Entity Type

Tierzucht

Number of Pages Required

1 page

Font styles to use
Sans Serif

Requirements
Must have
• Modern design that matches the logo
Nice to have
• Intuitive operation / Clear structure
Should not have
• No

```html
<!DOCTYPE html>
<html lang="en">
<head>
<meta charset="utf-8">
<title>Valle Alpacas</title>
<link rel="stylesheet" href="https://fonts.googleapis.com/css2?family=Raleway:wght@400;500;600;700&family=Abril+Fatface&family=Sacramento&display=swap">
<style>
  :root {
    --navy: #0f2744;
    --navy-deep: #0b1f38;
    --green: #7cbb3a;
    --green-dark: #5f9a26;
    --sky: #e4edf6;
    --paper: #f6f4f1;
    --bar: #4b4b4d;
    --ink: #2c3440;
    --muted: #5a6170;
    --line: #c7ccd4;
    --white: #ffffff;
  }
  * { box-sizing: border-box; margin: 0; padding: 0; }
  html, body { width: 1200px; height: 4237px; overflow: hidden; }
  body { position: relative; background: var(--white); font-family: "Raleway", sans-serif; color: var(--ink); }
  .abs { position: absolute; }
  .script { font-family: "Sacramento", cursive; font-weight: 400; }
  .btn { position: absolute; display: flex; align-items: center; justify-content: center; background: var(--navy); color: var(--white); font-size: 11.5px; font-weight: 600; border-radius: 5px; }
  .eyebrow { position: absolute; font-size: 8px; letter-spacing: 1.2px; color: #9aa1ad; text-transform: uppercase; display: flex; align-items: center; gap: 6px; }
  .eyebrow::after { content: ""; width: 30px; height: 1px; background: #9aa1ad; }
  .eyebrow i { width: 4px; height: 4px; border-radius: 50%; background: #9aa1ad; margin-left: -6px; }
  .copy { position: absolute; font-size: 11.2px; line-height: 16.6px; color: var(--muted); }
  .copy p + p { margin-top: 12px; }
  .photo { position: absolute; }

  /* top bar */
  .topbar { left: 0; top: 0; width: 1200px; height: 30px; background: var(--bar); color: var(--white); font-size: 10px; font-weight: 500; }
  .topbar span { position: absolute; top: 9px; }
  .search-line { position: absolute; left: 728px; top: 22px; width: 128px; height: 1px; background: #8a8a8c; }

  /* header */
  .header-bg { left: 0; top: 30px; width: 1200px; height: 88px; background: var(--paper); }
  .nav { left: 0; top: 98px; width: 1200px; height: 36px; }
  .nav a { position: absolute; top: 11px; color: var(--white); font-size: 11.5px; font-weight: 600; text-decoration: none; }
  .logo { position: absolute; border-radius: 50%; background: var(--white); border: 2px solid var(--green); display: flex; align-items: center; justify-content: center; text-align: center; color: var(--navy); font-weight: 700; line-height: 1.05; }

  /* hero */
  .hero-left { left: 0; top: 118px; width: 602px; height: 476px; background: var(--sky); }
  .hero-title { left: 60px; width: 506px; text-align: center; color: var(--navy); }
  .hero-title .l { font-size: 54px; font-weight: 400; line-height: 52px; letter-spacing: -0.5px; }
  .hero-title .big { font-family: "Abril Fatface", serif; color: var(--green); font-size: 76px; line-height: 72px; }

  /* meet */
  .animals-bg { left: 0; top: 1263px; width: 1200px; height: 477px; background: var(--navy-deep); }
  .pill { left: 432px; top: 1235px; width: 336px; height: 52px; background: var(--sky); border-radius: 26px; display: flex; align-items: center; justify-content: center; color: var(--navy); font-size: 34px; }
  .card { position: absolute; top: 1337px; width: 260px; height: 327px; background: var(--white); border-radius: 6px; overflow: visible; }
  .card .img { position: absolute; left: 0; top: 0; width: 260px; height: 160px; border-radius: 6px 6px 0 0; }
  .card .label { position: absolute; left: -13px; top: 159px; width: 258px; height: 54px; background: var(--green); color: var(--white); font-size: 30px; padding: 10px 0 0 20px; }
  .card p { position: absolute; left: 20px; top: 241px; width: 225px; font-size: 10.5px; line-height: 16px; color: var(--muted); }
  .card .more { position: absolute; left: 20px; top: 293px; font-size: 10.5px; font-weight: 700; color: var(--navy); display: flex; gap: 5px; align-items: center; }

  /* contact */
  .contact-sky { left: 0; top: 2943px; width: 1200px; height: 420px; background: linear-gradient(#e6eef6, #eef2f0); }
  .field { position: absolute; height: 26px; border-bottom: 1px solid var(--line); font-size: 9px; color: #9aa1ad; padding: 2px 0 0 18px; }

  /* footer */
  .footer-bg { left: 0; top: 3814px; width: 1200px; height: 370px; background: var(--paper); }
  .fcol { position: absolute; top: 3952px; }
  .fcol h4 { font-size: 13px; font-weight: 600; color: var(--navy); margin-bottom: 12px; }
  .fcol li { list-style: none; font-size: 10px; color: var(--ink); line-height: 19px; }
  .social li { display: flex; align-items: center; gap: 12px; line-height: 30px; }
  .social b { width: 22px; height: 22px; border-radius: 50%; background: #dfe3e8; display: inline-block; }
  .bottombar { left: 0; top: 4184px; width: 1200px; height: 53px; background: var(--bar); color: var(--white); font-size: 10px; }
</style>
</head>
<body>

<!-- top bar -->
<div class="abs topbar">
  <svg class="abs" style="left:180px;top:8px" width="12" height="12" viewBox="0 0 24 24"><path fill="#fff" d="M6.6 10.8a15 15 0 0 0 6.6 6.6l2.2-2.2c.3-.3.7-.4 1-.2 1.1.4 2.3.6 3.6.6.6 0 1 .4 1 1V20c0 .6-.4 1-1 1A17 17 0 0 1 3 4c0-.6.4-1 1-1h3.5c.6 0 1 .4 1 1 0 1.3.2 2.5.6 3.6.1.3 0 .7-.2 1z"/></svg>
  <span style="left:202px">555-014-2870</span>
  <svg class="abs" style="left:305px;top:10px" width="11" height="9" viewBox="0 0 24 18"><rect x="1" y="1" width="22" height="16" rx="2" fill="#fff"/><path d="M2 2l10 8 10-8" stroke="#4b4b4d" stroke-width="2" fill="none"/></svg>
  <span style="left:329px">hello@vallealpacas.farm</span>
  <span style="left:728px;top:10px;font-size:8px;color:#d0d0d0">Search Here...</span>
  <svg class="abs" style="left:843px;top:8px" width="11" height="11" viewBox="0 0 24 24"><circle cx="10" cy="10" r="7" stroke="#bbb" stroke-width="2.5" fill="none"/><path d="M15 15l7 7" stroke="#bbb" stroke-width="2.5"/></svg>
  <div class="search-line"></div>
  <svg class="abs" style="left:912px;top:9px" width="11" height="12" viewBox="0 0 24 24"><circle cx="12" cy="7" r="5" stroke="#fff" stroke-width="2" fill="none"/><path d="M3 23c0-5 4-8 9-8s9 3 9 8" stroke="#fff" stroke-width="2" fill="none"/></svg>
  <span style="left:929px">My Account</span>
</div>

<!-- header -->
<div class="abs header-bg"></div>
<svg class="abs nav" width="1200" height="36" viewBox="0 0 1200 36">
  <polygon points="164,0 1036,0 1024,18 1036,36 164,36 176,18" fill="#0f2744"/>
  <line x1="184" y1="5" x2="1016" y2="5" stroke="#fff" stroke-width="1" stroke-dasharray="4 3" opacity=".7"/>
  <line x1="184" y1="31" x2="1016" y2="31" stroke="#fff" stroke-width="1" stroke-dasharray="4 3" opacity=".7"/>
</svg>
<nav class="abs nav">
  <a style="left:223px">Home</a>
  <a style="left:313px">About Us</a>
  <a style="left:409px">Our Animals</a>
  <a style="left:721px">Shop</a>
  <a style="left:805px">Alpaca Wool</a>
  <a style="left:928px">Contact</a>
</nav>
<div class="logo" style="left:524px;top:2px;width:152px;height:152px;font-size:19px">VALLE<br>ALPACAS</div>

<!-- hero -->
<section>
  <div class="abs hero-left"></div>
  <div class="abs" role="img" aria-label="Dark silhouette of two alpacas" style="left:0;top:430px;width:175px;height:164px;background:linear-gradient(#e4edf6 10%,#d6e0eb)"></div>
  <div class="photo" role="img" aria-label="Photo of a fluffy white alpaca against a green field" style="left:602px;top:118px;width:598px;height:476px;background:linear-gradient(120deg,#5a6a3a,#b9b39b 45%,#e8e2d6 60%,#7a8652)"></div>
  <div class="eyebrow" style="left:190px;top:215px;color:var(--navy);letter-spacing:.8px">
    <i style="background:var(--navy);margin:0"></i><span style="width:30px;height:1px;background:var(--navy)"></span>Welcome to Valle-Alpacas where
  </div>
  <div class="abs hero-title" style="top:232px">
    <div class="l">Alpacas Roam</div>
    <div class="l">and Dreams</div>
    <div class="big">Take Flight</div>
  </div>
  <p class="abs" style="left:130px;top:414px;width:366px;text-align:center;font-size:11px;line-height:16px;color:var(--muted)">Welcome to Valle-Alpacas, where the tranquility of the country side meets the grace of alpacas.</p>
  <div class="btn" style="left:227px;top:465px;width:174px;height:41px">Meet Our Beloved Alpacas</div>
</section>

<!-- intro -->
<section>
  <div class="abs" style="left:209px;top:666px;width:370px;height:493px;background:#fff;box-shadow:0 6px 24px rgba(0,0,0,.14)"></div>
  <div class="photo" role="img" aria-label="Photo of a young brown alpaca in a meadow" style="left:223px;top:682px;width:341px;height:460px;background:linear-gradient(160deg,#6b7a3c,#a67a4c 50%,#7d8f45)"></div>
  <div class="abs" style="left:136px;top:912px;width:146px;height:172px;background:#fff;box-shadow:0 4px 14px rgba(0,0,0,.2);transform:rotate(-6deg)">
    <div role="img" aria-label="Photo of crocheted alpaca wool toys" style="margin:8px;height:136px;background:linear-gradient(135deg,#8a6a58,#c9a590)"></div>
  </div>
  <div class="logo" style="left:519px;top:761px;width:112px;height:112px;font-size:13px">VALLE<br>ALPACAS</div>
  <div class="eyebrow" style="left:676px;top:696px">Introduction</div>
  <h2 class="abs script" style="left:676px;top:712px;font-size:46px;color:var(--navy);white-space:nowrap">Welcome to Valle-<span style="color:var(--green)">Alpacas</span></h2>
  <div class="copy" style="left:676px;top:780px;width:362px">
    <p>Welcome to Valle-Alpacas, where the tranquility of the countryside meets the grace of alpacas. Nestled in the heart of our farm is a sanctuary for these gentle creatures. But Valle-Alpacas is more than just a place; it's a mission—a commitment to sustainable farming, animal welfare, and the preservation of traditional craftsmanship. Join us on a journey through our farm, meet our beloved animals, and discover the story behind our</p>
    <p style="margin-top:12px;color:var(--ink);font-weight:600">Our Mission :</p>
    <p style="margin-top:2px">At Valle-Alpacas, our mission is simple yet profound: to cultivate a harmonious relationship between humans, animals, and nature. We believe in the power of ethical farming practices and the transformative potential of connecting with animals. By nurturing our alpacas with love and respect, we aim to promote their well-being while sharing the beauty of their existence with the world. Through our farm and future endeavors, we strive to inspire others to embrace sustainability, compassion, and the joy of living in harmony with the natural world.</p>
  </div>
  <div class="btn" style="left:676px;top:1103px;width:174px;height:41px">Meet Our Beloved Alpacas</div>
</section>

<!-- animals -->
<section>
  <div class="abs animals-bg"></div>
  <h2 class="abs pill script">Meet Our Animals</h2>
  <article class="card" style="left:181px">
    <div class="img" role="img" aria-label="Photo of a brown stallion grazing on grass" style="background:linear-gradient(#a9c3d6,#7aa24a 55%,#5e8a34)"></div>
    <h3 class="label script">Stallions</h3>
    <p>With his striking coat and noble demeanor, he commands attention wherever he goes. As a cornerstone of our breeding program.</p>
    <span class="more"><svg width="10" height="10" viewBox="0 0 10 10"><path d="M1 5h7M5 2l3 3-3 3" stroke="#7cbb3a" stroke-width="1.6" fill="none"/></svg>Read More</span>
  </article>
  <article class="card" style="left:477px">
    <div class="img" role="img" aria-label="Photo of a chestnut mare with her foal" style="background:linear-gradient(#c7d3de,#b98a5a 50%,#8ea457)"></div>
    <h3 class="label script">Our Mares</h3>
    <p>With her nurturing instincts and gentle nature, she plays a vital role in fostering the next generation of alpacas.</p>
    <span class="more"><svg width="10" height="10" viewBox="0 0 10 10"><path d="M1 5h7M5 2l3 3-3 3" stroke="#7cbb3a" stroke-width="1.6" fill="none"/></svg>Read More</span>
  </article>
  <article class="card" style="left:773px">
    <div class="img" role="img" aria-label="Photo of a group of alpacas by a barn" style="background:linear-gradient(#9fb1c4,#8a7460 50%,#c9bca6)"></div>
    <h3 class="label script">Valle-Alpacas</h3>
    <p>Alpacas are captivating and gentle creatures known for their friendly nature and luxurious fleece.</p>
    <span class="more"><svg width="10" height="10" viewBox="0 0 10 10"><path d="M1 5h7M5 2l3 3-3 3" stroke="#7cbb3a" stroke-width="1.6" fill="none"/></svg>Read More</span>
  </article>
</section>

<!-- for sale -->
<section>
  <div class="eyebrow" style="left:131px;top:1895px">For Sale</div>
  <h2 class="abs script" style="left:131px;top:1912px;font-size:44px;line-height:42px;color:var(--navy)">Valle-Alpacas Future<br><span style="color:var(--green)">Expansion</span></h2>
  <div class="copy" style="left:131px;top:2021px;width:356px">
    <p>At Valle-Alpacas, we occasionally offer select animals for sale to discerning enthusiasts and fellow breeders. Please contact us for current availability and pricing. Each alpaca comes with a pedigree, health guarantee, and lifetime support from our experienced team.</p>
    <p>While Valle-Alpacas currently focuses on alpaca breeding and care, we have ambitious plans for the future. Stay tuned for the launch of our webshop, where you'll find a curated selection of exquisite products crafted from our alpaca wool. From cozy blankets to luxurious garments, each item is a testament to the timeless beauty and unparalleled quality of alpaca fiber. By supporting our webshop, you'll not only indulge in luxurious comfort but also contribute to the sustainability of our farm and the livelihood of our beloved alpacas.</p>
  </div>
  <div class="btn" style="left:131px;top:2280px;width:175px;height:41px">Meet Our Beloved Alpacas</div>
  <div class="photo" role="img" aria-label="Photo of an alpaca with a red fringe before snowy mountains" style="left:520px;top:1810px;width:680px;height:598px;background:linear-gradient(135deg,#f2f2f2 5%,#9fb3b8 30%,#b0773e 60%,#d8c6a4);border-radius:40% 0 0 30%"></div>
</section>

<!-- wool -->
<section>
  <div class="photo" role="img" aria-label="Photo of grey and cream alpaca wool skeins with pine cones" style="left:0;top:2408px;width:592px;height:535px;background:linear-gradient(120deg,#8a4a35,#a8a8aa 40%,#e8dcc4 70%,#f4f1ec);border-radius:0 40% 45% 0"></div>
  <div class="eyebrow" style="left:707px;top:2569px">Coming Up</div>
  <h2 class="abs script" style="left:707px;top:2588px;font-size:46px;color:var(--navy)">Alpaca Wool <span style="color:var(--green)">Products</span></h2>
  <div class="copy" style="left:707px;top:2664px;width:358px">
    <p>Alpaca wool is renowned for its exceptional softness, warmth, and durability. Unlike sheep's wool, alpaca fiber is hypoallergenic, making it suitable for sensitive skin. At Valle-Alpacas, we transform this luxurious fiber into a range of exquisite products, including cozy blankets, elegant scarves, and stylish garments. Each item is crafted with care, reflecting the natural beauty and superior quality of alpaca wool, providing comfort and elegance in every stitch. Stay tuned for our future webshop, where you can experience the timeless appeal of alpaca wool products.</p>
  </div>
  <div class="btn" style="left:707px;top:2833px;width:199px;height:43px">Explore More Alpacas Products</div>
</section>

<!-- contact -->
<section>
  <div class="abs contact-sky"></div>
  <div class="abs" role="img" aria-label="Painted landscape of sheep grazing on golden hills" style="left:0;top:3330px;width:1200px;height:484px;background:linear-gradient(#c9cdb4,#b3a548 25%,#8b8f2e 60%,#4d5a24)"></div>
  <div class="eyebrow" style="left:535px;top:3049px;gap:0">
    <i style="margin:0 6px 0 0"></i><span style="width:30px;height:1px;background:#9aa1ad;margin-right:6px"></span>Contact Us
  </div>
  <h2 class="abs script" style="left:0;top:3066px;width:1200px;text-align:center;font-size:46px;color:var(--navy)">Get In Touch <span style="color:var(--green)">With Us</span></h2>
  <p class="abs" style="left:330px;top:3132px;width:540px;text-align:center;font-size:11px;line-height:17px;color:var(--muted)">We would love to hear from you! Whether you have questions about our farm, our alpacas, or our future alpaca wool products, feel free to reach out to us. Here's how you can get in touch:</p>
  <div class="field" style="left:326px;top:3200px;width:262px">Full Name*</div>
  <div class="field" style="left:612px;top:3200px;width:262px">Email*</div>
  <div class="field" style="left:326px;top:3239px;width:262px">Phone*</div>
  <div class="field" style="left:612px;top:3239px;width:262px">Address*</div>
  <div class="field" style="left:326px;top:3278px;width:548px">Message*</div>
  <div class="btn" style="left:513px;top:3336px;width:174px;height:41px">Submit Request</div>
</section>

<!-- footer -->
<footer>
  <div class="abs footer-bg"></div>
  <div class="fcol" style="left:151px"><h4>Navigation</h4><ul><li>Home</li><li>About Us</li><li>Our Animals</li><li>Shop</li><li>Alpaca Wool</li><li>Contact</li></ul></div>
  <div class="fcol" style="left:275px"><h4>Animals</h4><ul><li>Alpacas</li><li>Stallion</li><li>Mares</li></ul></div>
  <div class="fcol" style="left:388px"><h4>Valle Alpacas</h4><ul><li>See us in Action</li><li>Reviews</li><li>FAQ</li><li>Test Videos</li><li>Video Gallery</li></ul></div>
  <div class="fcol" style="left:549px"><h4>Company</h4><ul><li>About</li><li>Reviews</li><li>Contact Us</li></ul></div>
  <div class="fcol social" style="left:679px"><h4 style="margin-bottom:4px">Social Media</h4><ul><li><b></b>Community</li><li><b></b>Updates</li><li><b></b>Photos</li></ul></div>
  <div class="fcol" style="left:829px"><h4 style="line-height:16px">Join Our Mailing List For Updates<br>About Pets!</h4></div>
  <div class="abs" style="left:820px;top:4006px;width:211px;height:30px;background:#ebebeb;border-radius:4px;font-size:8px;color:#9aa1ad;padding:10px 0 0 18px">Email...</div>
  <div class="abs" style="left:820px;top:4049px;width:211px;height:30px;background:var(--green);border-radius:4px;color:#fff;font-size:11px;font-weight:600;display:flex;align-items:center;justify-content:center">Subscribe</div>
  <div class="abs bottombar">
    <span class="abs" style="left:153px;top:23px">Copyright © Valle-Alpacas 2024. All rights reserved.</span>
    <span class="abs" style="left:880px;top:23px">Privacy Policy &amp; Terms of Use</span>
  </div>
  <div class="logo" style="left:534px;top:4085px;width:132px;height:132px;font-size:16px">VALLE<br>ALPACAS</div>
</footer>

</body>
</html>
```